Wattle Glen Manor Brochure Design

We need a brochure designed for our Aged Care Facility. We need designs that portray warmth and welcoming and at the same time something professional. We have attached the previous brochure and are looking for a modern professional brochure. We are not set on sizing and welcome ideas.

Attachments:
- One more high res photo is available via this link: https://www.filevaultex.net/s/kq52wpx9trmbe3n/Manor_High-Res_18.jpg?dl=0
- Another high res file has been added and is available through this link:
https://www.filevaultex.net/s/mv71cnd8yhsue6r/Manor_High-Res_24.jpg?dl=0

Target Market(s)

Aged Care and families

Requirements
Must have
• Logo and contact details

```html
<!DOCTYPE html>
<html lang="en">
<head>
<meta charset="utf-8">
<title>Wattle Glen Manor – Tri-fold Brochure</title>
<link href="https://fonts.googleapis.com/css2?family=Oswald:wght@500;600&family=Lato:ital,wght@0,400;0,700;1,400&family=Archivo+Black&display=swap" rel="stylesheet">
<style>
  :root{
    --slate:#4d7286;
    --slate-dark:#3f5f70;
    --taupe:#9b8f86;
    --ink:#2f3a40;
    --paper:#ffffff;
    --mist:#f1f3f4;
    --stage:#dcdedb;
    --sky:#2f83c9;
  }
  *{margin:0;padding:0;box-sizing:border-box}
  html,body{width:1200px;height:1108px;overflow:hidden;background:var(--stage)}
  .brochure{position:absolute;left:30px;top:151px;width:1140px;height:806px;background:var(--paper);box-shadow:0 6px 24px rgba(0,0,0,.18);font-family:"Lato",sans-serif}
  .brochure-art{position:absolute;inset:0}
  .panel{position:absolute;top:0;width:380px;height:806px}
  .panel-back{left:0}
  .panel-inside{left:380px}
  .panel-cover{left:760px}

  .section-title{position:absolute;left:0;width:380px;text-align:center;font-family:"Oswald",sans-serif;font-weight:600;color:var(--paper);font-size:40px;line-height:1.2;letter-spacing:.5px}
  .section-text{position:absolute;left:45px;width:290px;text-align:center;color:var(--paper);font-size:12.5px;line-height:1.4}
  .mission-title{top:432px}
  .mission-text{top:488px}
  .commitment-title{top:630px}
  .commitment-text{top:686px}

  .testimonial-block{position:absolute;left:42px;top:22px;width:304px;color:var(--paper)}
  .quote-mark{display:block;font-family:"Archivo Black",sans-serif;color:var(--paper);font-size:48px;line-height:.8;height:32px}
  .quote-close{text-align:right;margin-top:2px;height:30px}
  .testimonial{font-size:12.5px;line-height:1.34}
  .testimonial-author{margin-top:10px;padding-left:18px;font-size:12px;line-height:1.35}
  .testimonial-author strong{font-weight:700}

  .badge-name{position:absolute;left:490px;top:395px;width:160px;text-align:center;font-family:"Oswald",sans-serif;font-weight:500;font-size:21px;line-height:1.15;color:var(--slate);letter-spacing:.5px}

  .contact{position:absolute;left:0;top:612px;width:380px;color:var(--ink);font-size:14px;line-height:1.9;text-align:center;font-style:normal}
  .contact svg{width:12px;height:12px;vertical-align:-1px;margin-right:4px;fill:var(--slate)}
  .contact-row span{margin:0 8px}

  .cover-name{position:absolute;left:0;top:40px;width:380px;text-align:center;font-family:"Oswald",sans-serif;font-weight:500;font-size:26px;color:var(--paper);letter-spacing:1px}
  .headline{position:absolute;left:20px;top:505px;width:340px;text-align:center;line-height:1;white-space:nowrap}
  .headline-line{display:block}
  .headline-top{font-family:"Archivo Black",sans-serif;font-size:42px;color:var(--ink);letter-spacing:1px}
  .headline-mid{font-family:"Oswald",sans-serif;font-weight:600;font-size:40px;color:var(--ink);margin-top:4px}
  .headline-accent{font-family:"Oswald",sans-serif;font-weight:600;font-size:52px;color:var(--slate);margin-top:4px}
  .cover-url{position:absolute;left:0;top:705px;width:380px;text-align:center;font-size:13px;letter-spacing:5px;color:var(--ink)}
</style>
</head>
<body>
<main class="brochure">
  <svg class="brochure-art" width="1140" height="806" viewBox="0 0 1140 806">
    <defs>
      <linearGradient id="handsPhoto" x1="0" y1="0" x2="1" y2="1">
        <stop offset="0" stop-color="#a9c6cf"/>
        <stop offset=".45" stop-color="#e3c7b8"/>
        <stop offset="1" stop-color="#f2e4dc"/>
      </linearGradient>
      <linearGradient id="courtyardPhoto" x1="0" y1="0" x2="0" y2="1">
        <stop offset="0" stop-color="#2f83c9"/>
        <stop offset=".45" stop-color="#6aa6d4"/>
        <stop offset=".7" stop-color="#8a9a7a"/>
        <stop offset="1" stop-color="#5f7a4a"/>
      </linearGradient>
      <linearGradient id="paperSheen" x1="0" y1="0" x2="1" y2="1">
        <stop offset="0" stop-color="#ffffff"/>
        <stop offset="1" stop-color="#eef1f3"/>
      </linearGradient>
      <clipPath id="backPanelClip"><rect x="0" y="0" width="380" height="806"/></clipPath>
    </defs>

    <rect class="photo-hands" x="0" y="0" width="380" height="400" fill="url(#handsPhoto)" role="img" aria-label="Photo: close-up of an elderly hand gently holding another hand"/>
    <rect class="testimonial-bg" x="380" y="0" width="380" height="420" fill="var(--slate)"/>
    <rect class="photo-courtyard" x="760" y="0" width="380" height="470" fill="url(#courtyardPhoto)" role="img" aria-label="Photo: the manor courtyard with gum trees, a timber pergola and a paved path under blue sky"/>

    <path class="wave-taupe" d="M0 350 C 220 320, 420 410, 580 405 S 930 385, 1140 445 L1140 806 L0 806 Z" fill="var(--taupe)"/>
    <path class="wave-slate-line" d="M760 398 C 880 392, 1020 410, 1140 430 L1140 446 C 1020 428, 880 408, 760 412 Z" fill="var(--slate)"/>
    <path class="wave-white" d="M0 366 C 220 336, 420 426, 580 421 S 930 401, 1140 461 L1140 806 L0 806 Z" fill="url(#paperSheen)"/>
    <g clip-path="url(#backPanelClip)">
      <path class="wave-slate" d="M0 374 C 220 344, 420 434, 580 429 S 930 409, 1140 469 L1140 806 L0 806 Z" fill="var(--slate)"/>
    </g>
    <line x1="380" y1="420" x2="380" y2="806" stroke="#d6dadd" stroke-width="1"/>
    <line x1="760" y1="470" x2="760" y2="806" stroke="#d6dadd" stroke-width="1"/>

    <circle class="badge-ring" cx="570" cy="420" r="108" fill="var(--taupe)"/>
    <circle cx="570" cy="420" r="100" fill="var(--paper)"/>
    <circle cx="570" cy="420" r="92" fill="none" stroke="var(--slate)" stroke-width="6"/>
  </svg>

  <section class="panel panel-back">
    <h2 class="section-title mission-title">MISSION</h2>
    <p class="section-text mission-text">To continue to provide a home for persons in need of constant nursing care and to afford each individual resident not only the respect and dignity to which all humankind has a right, but to make their later years in life enjoyable, filled with laughter and to maintain the rightful place as respected members of our community.</p>
    <h2 class="section-title commitment-title">COMMITMENT</h2>
    <p class="section-text commitment-text">We make it our commitment to continue seeking out employment opportunities, resources and education to enhance all of our values.</p>
  </section>

  <section class="panel panel-inside">
    <blockquote class="testimonial-block">
      <span class="quote-mark quote-open">&ldquo;</span>
      <p class="testimonial">Edith talks more, laughs more, her posture has improved, she is standing more upright. Thankfully the earlier the depression is no longer evident. Every one of us has noticed how much our mother has changed &amp; it is a huge change for the better. We feel blessed that we have our mother in a facility where she is happy and is taken care of. Everyone who sees mum has remarked on how much she has changed (since moving to WGM), how happy she appears to be – a huge change for the better.</p>
      <span class="quote-mark quote-close">&rdquo;</span>
      <p class="testimonial-author"><strong>Maree Holloway</strong><br>(Edith's eldest daughter) <strong>June 2013</strong></p>
    </blockquote>
  </section>

  <div class="badge-name">Wattle Glen<br>Manor</div>

  <section class="panel panel-inside">
    <address class="contact">
      <div class="contact-row"><svg viewBox="0 0 12 12"><path d="M6 0a4 4 0 0 0-4 4c0 3 4 8 4 8s4-5 4-8a4 4 0 0 0-4-4zm0 5.5A1.5 1.5 0 1 1 6 2.5a1.5 1.5 0 0 1 0 3z"/></svg>27 Banksia Crescent Wattle Glen VIC 3096</div>
      <div class="contact-row">
        <span><svg viewBox="0 0 12 12"><rect x="3" y="0" width="6" height="12" rx="1.5"/></svg>(03) 9438 5172</span>
        <span><svg viewBox="0 0 12 12"><rect x="0" y="4" width="12" height="6" rx="1"/><rect x="3" y="1" width="6" height="3"/></svg>(03) 9438 5173</span>
      </div>
      <div class="contact-row"><svg viewBox="0 0 12 12"><circle cx="6" cy="6" r="5.5"/></svg>www.wattleglenmanor.com.au</div>
    </address>
  </section>

  <section class="panel panel-cover">
    <div class="cover-name">Wattle Glen Manor</div>
    <h1 class="headline">
      <span class="headline-line headline-top">WE HAVE</span>
      <span class="headline-line headline-mid">LIVED TOGETHER</span>
      <span class="headline-line headline-accent">FOR 50 YEARS</span>
    </h1>
    <p class="cover-url">www.wattleglenmanor.com.au</p>
  </section>
</main>
</body>
</html>
```